Harbor Nightclub

Nightclub flyer., digital single sided, for KV and PX. I included samples of some previous flyers we've used. Sample Info:
HARBOR
FRIDAYS
FRI MAY 1 2020
DJ VORTAN (club floor)
DJ RUZO & DJ TAV (residents on the lounge floor)
4217 Marlow Avenue Sacramento
www.harborvenuehall.example for list/VIP inquiries

Target Market(s)

Upscale top 40 crowd but want some cool and artsy like the examples included.

Font styles to use
Sans Serif

Requirements
Must have
• Harbor Logo
Nice to have
• Would be nice if the flyer can be incorporated later with DJ photos (sometimes we will add dj photos to pixagram etc). Would like a big city type of feel.
Should not have
• Nothing too sexual.

```html
<!DOCTYPE html>
<html lang="en">
<head>
<meta charset="utf-8">
<title>Harbor Fridays</title>
<link rel="stylesheet" href="https://fonts.googleapis.com/css2?family=Montserrat:wght@300;400;600;700&family=Raleway:wght@200;300&display=swap">
<style>
  :root {
    --ink: #ffffff;
    --night-top: #2a1d8f;
    --night-mid: #3a1f9a;
    --haze-cyan: #39c6e6;
    --haze-violet: #6a3cc8;
    --smoke: #f1e9f4;
    --floor-dark: #150a14;
    --floor-ember: #3e1a16;
    --neon: #c535e8;
    --page: #ffffff;
  }
  * { margin: 0; padding: 0; box-sizing: border-box; }
  html, body { width: 848px; height: 1200px; overflow: hidden; background: var(--page); }
  .flyer {
    position: relative;
    width: 848px;
    height: 1200px;
    overflow: hidden;
    color: var(--ink);
    font-family: "Montserrat", sans-serif;
  }
  .scene-photo {
    position: absolute; inset: 0;
    background:
      radial-gradient(ellipse 130px 90px at 90px 560px, rgba(241,233,244,0.85), rgba(241,233,244,0) 70%),
      radial-gradient(ellipse 140px 90px at 760px 540px, rgba(230,230,235,0.85), rgba(230,230,235,0) 70%),
      radial-gradient(ellipse 180px 240px at 420px 420px, rgba(57,198,230,0.55), rgba(57,198,230,0) 70%),
      radial-gradient(ellipse 120px 300px at 230px 260px, rgba(57,198,230,0.35), rgba(57,198,230,0) 70%),
      radial-gradient(ellipse 200px 60px at 720px 800px, rgba(241,220,240,0.45), rgba(241,220,240,0) 70%),
      linear-gradient(180deg, var(--night-top) 0%, var(--night-mid) 45%, var(--haze-violet) 62%, #3a1560 72%, var(--floor-dark) 88%, var(--floor-dark) 100%),
      linear-gradient(90deg, var(--floor-ember), transparent);
  }
  .scene-photo::after {
    content: ""; position: absolute; inset: 0;
    background: linear-gradient(20deg, rgba(62,26,22,0.7) 0%, rgba(62,26,22,0) 35%);
  }
  .neon-frame { position: absolute; inset: 0; width: 848px; height: 1200px; }
  .venue-title {
    position: absolute; top: 112px; left: 0; width: 848px;
    text-align: center;
    font-family: "Raleway", sans-serif; font-weight: 300;
    font-size: 90px; letter-spacing: 26px; padding-left: 26px;
    line-height: 1;
  }
  .night-name {
    position: absolute; top: 700px; left: 0; width: 848px;
    text-align: center;
    font-family: "Raleway", sans-serif; font-weight: 200;
    font-size: 94px; letter-spacing: 4px; line-height: 1;
  }
  .event-date {
    position: absolute; top: 820px; left: 0; width: 848px;
    text-align: center;
    font-family: "Montserrat", sans-serif; font-weight: 400;
    font-size: 24px; letter-spacing: 10px; padding-left: 10px; line-height: 1;
  }
  .headliner {
    position: absolute; top: 874px; left: 0; width: 848px;
    text-align: center;
    font-weight: 700; font-size: 100px; letter-spacing: -3px; line-height: 1.1;
  }
  .support-acts {
    position: absolute; top: 1012px; left: 0; width: 848px; height: 50px;
    font-weight: 400; font-size: 44px; letter-spacing: -1px; line-height: 50px;
  }
  .support-acts span { position: absolute; top: 0; transform: translateX(-50%); white-space: nowrap; }
  .support-acts .act-one { left: 266px; }
  .support-acts .divider { left: 413px; }
  .support-acts .act-two { left: 570px; }
  .venue-address {
    position: absolute; top: 1126px; left: 183px;
    font-weight: 400; font-size: 15px; letter-spacing: 7px; line-height: 1; white-space: nowrap;
  }
  .venue-mark {
    position: absolute; top: 1066px; left: 696px; width: 104px;
    text-align: center;
  }
  .venue-mark .mark-dot {
    display: block; width: 30px; height: 30px; margin: 0 auto 14px;
    border-radius: 50%; background: var(--ink);
  }
  .venue-mark .mark-name {
    font-weight: 400; font-size: 20px; letter-spacing: 1px; line-height: 1;
  }
</style>
</head>
<body>
  <main class="flyer">
    <div class="scene-photo" role="img" aria-label="Blurred nightclub interior in violet and cyan light with soft clouds of smoke drifting across the dance floor"></div>

    <svg class="neon-frame" viewBox="0 0 848 1200" aria-hidden="true">
      <polygon points="392,264 219,539 236,637 676,579" fill="none" stroke="var(--neon)" stroke-width="3" stroke-linejoin="round"/>
    </svg>

    <h1 class="venue-title">HARBOR</h1>
    <h2 class="night-name">FRIDAYS</h2>
    <p class="event-date">MAY 1 2020</p>
    <p class="headliner">DJ VORTAN</p>
    <p class="support-acts">
      <span class="act-one">DJ RUZO</span>
      <span class="divider">|</span>
      <span class="act-two">DJ TAV</span>
    </p>
    <p class="venue-address">4217 Marlow Avenue Sacramento</p>
    <div class="venue-mark">
      <span class="mark-dot"></span>
      <span class="mark-name">HARBOR</span>
    </div>
  </main>
</body>
</html>
```